Flyer-Design für syrisch-orthodoxe Kirche in Österreich
Super schnell und auf alle Wünsche bestens reagiert!
Zielgruppe
Wir sind eine Pfarre die gerade dabei ist den ersten Neubau der Aramäischen Gemeindekirche in Österreich, in welcher die Muttersprache Jesu gesprochen wird, zu errichten.
Ausführliche Informationen über unsere Gemeinde sowie unser Vorhaben findet ihr in den angehängten Dateien.
Aufgabenstellung
Textvorlagen sowie das angedachte Format sind in den Anhängen vorhanden und erläutert.
Aber auch Querdenker sind sehr gerne eingeladen ihre eigenen Ideen zu präsentieren :)
Wir werden versuchen so rasch wie möglich auf die Entwürfe bzw. auch auf Fragen zu reagieren um gemeinsam ein optimales Ergebnis zu erreichen!
EDIT:
Bitte den öffentlichen Kommentar beachten!

```html
<!DOCTYPE html>
<html lang="de">
<head>
<meta charset="utf-8">
<title>Spendenflyer Kirchenbau – Pfarrei Heiliger Ephräm</title>
<link rel="stylesheet" href="https://fonts.googleapis.com/css2?family=Open+Sans:ital,wght@0,400;0,600;0,700;1,600;1,700&display=swap">
<style>
:root{
  --gold:#b8891e;
  --white:#ffffff;
  --ink:#1d1d1d;
  --grey:#4a4a4a;
  --sky-top:#6f97d4;
  --sky-mid:#a9c0e4;
  --stone:#ece9e2;
  --stone-shade:#d8d4cb;
  --blue-panel:#a6b6da;
  --blue-panel-light:#c8d1e6;
  --form-red:#e8664f;
  --form-pink:#fbe3dc;
  --shadow:rgba(0,0,0,.28);
}
*{box-sizing:border-box;margin:0;padding:0}
html,body{width:1200px;height:1200px;overflow:hidden;background:var(--white)}
body{font-family:"Open Sans",Arial,sans-serif}
.canvas{position:relative;width:1200px;height:1200px;background:var(--white);overflow:hidden}
.sheet{position:absolute;background:var(--white);box-shadow:0 2px 8px var(--shadow)}
.sheet--outside{left:42px;top:92px;width:1119px;height:459px}
.sheet--inside{left:42px;top:620px;width:1121px;height:460px}
.art{position:absolute;display:block}
.art--outside{left:49px;top:98px}
.art--inside{left:49px;top:627px}
.t{position:absolute}
.brandline{position:absolute;display:flex;align-items:center;gap:6px;font-weight:700;font-size:7.4px;color:var(--ink);white-space:nowrap}
.brandline .mark{width:14px;height:14px;border:1.2px solid var(--ink);border-radius:50%;display:block}

.verse-ref{left:66px;top:424px;font-weight:700;font-style:italic;font-size:12.5px;line-height:15px;color:var(--ink)}
.verse{left:66px;top:463px;width:135px;font-weight:600;font-style:italic;font-size:8.6px;line-height:12px;color:var(--ink)}

.pitch{left:504px;top:266px;width:160px;font-size:8.3px;line-height:12px;color:var(--gold)}
.banner-title{left:504px;top:380px;font-size:14.5px;font-weight:400;color:var(--white);letter-spacing:.2px}
.account{left:504px;top:421px;width:300px;font-size:6px;line-height:7.4px;color:var(--grey)}
.account p{margin-bottom:5px}
.account .thanks{font-size:7.3px;margin-top:6px}

.band-parish{left:720px;top:432px;width:195px;text-align:right;font-size:15.5px;line-height:18px;color:var(--white)}
.band-appeal{left:949px;top:432px;font-size:15.5px;line-height:18px;color:var(--white)}
.contact{left:760px;top:484px;width:155px;text-align:right;font-size:8.3px;line-height:12px;color:var(--gold)}
.appeal-text{left:949px;top:484px;width:160px;font-size:8.3px;line-height:12px;color:var(--gold)}

.h{position:absolute;font-weight:700;font-size:13px;line-height:16px;color:var(--gold);letter-spacing:.2px}
.body{position:absolute;font-size:7.2px;line-height:9px;color:var(--white);text-align:justify}
.body p{margin-bottom:9px}
.who-h{left:66px;top:652px}
.who{left:66px;top:677px;width:188px}
.why-h{left:288px;top:760px}
.why{left:288px;top:818px;width:190px}
.proj-h{left:520px;top:760px;width:125px;text-align:right}
.proj{left:511px;top:818px;width:190px}
.do-h{left:735px;top:652px}
.do-intro{left:735px;top:677px;width:188px;text-align:left}
.do-list{position:absolute;left:735px;top:714px;width:190px;list-style:none;font-size:6.6px;line-height:8px;color:var(--white)}
.do-list li{position:relative;padding-left:11px;margin-bottom:5.5px}
.do-list li::before{content:"";position:absolute;left:1px;top:2.5px;width:3px;height:3px;border-radius:50%;background:var(--white)}

.form{position:absolute;left:940px;top:627px;width:215px;height:447px;background:var(--white)}
.form svg{display:block}
</style>
</head>
<body>
<div class="canvas">

  <div class="sheet sheet--outside"></div>
  <svg class="art art--outside" width="1106" height="446" viewBox="0 0 1106 446">
    <defs>
      <linearGradient id="sky" x1="0" y1="0" x2="0" y2="1">
        <stop offset="0" stop-color="var(--sky-top)"/>
        <stop offset=".3" stop-color="var(--sky-mid)"/>
        <stop offset=".55" stop-color="var(--stone)"/>
        <stop offset=".85" stop-color="var(--stone-shade)"/>
        <stop offset="1" stop-color="#f2f1ee"/>
      </linearGradient>
      <radialGradient id="buildingGlow" cx=".5" cy=".6" r=".55">
        <stop offset="0" stop-color="#f7f5f0"/>
        <stop offset=".6" stop-color="#ebe7de" stop-opacity=".8"/>
        <stop offset="1" stop-color="#ebe7de" stop-opacity="0"/>
      </radialGradient>
      <linearGradient id="warmDoor" x1="0" y1="0" x2="0" y2="1">
        <stop offset="0" stop-color="#c98f2a" stop-opacity="0"/>
        <stop offset="1" stop-color="#b07a22" stop-opacity=".35"/>
      </linearGradient>
    </defs>
    <g role="img" aria-label="Rendering der neuen Kirche mit zwei Kuppeltürmen vor blauem Himmel">
      <rect x="0" y="0" width="437" height="446" fill="url(#sky)"/>
      <rect x="0" y="60" width="437" height="340" fill="url(#buildingGlow)"/>
      <rect x="180" y="300" width="257" height="90" fill="url(#warmDoor)"/>
    </g>
    <g role="img" aria-label="Rendering des Kirchenbaus aus hellem Stein mit Kuppelturm">
      <rect x="437" y="0" width="447" height="446" fill="url(#sky)"/>
      <rect x="437" y="40" width="447" height="320" fill="url(#buildingGlow)"/>
    </g>
    <g role="img" aria-label="Rendering eines Kuppelturms der neuen Kirche vor Wolkenhimmel">
      <rect x="884" y="0" width="222" height="446" fill="url(#sky)"/>
      <rect x="884" y="50" width="222" height="330" fill="url(#buildingGlow)"/>
    </g>
    <polygon points="0,264 232,446 0,446" fill="var(--white)"/>
    <polygon points="437,52 700,274 437,274" fill="var(--white)"/>
    <rect x="437" y="274" width="447" height="172" fill="var(--white)"/>
    <rect x="884" y="378" width="222" height="68" fill="var(--white)"/>
    <polygon points="437,274 725,274 682,309 437,309" fill="var(--gold)"/>
    <polygon points="726,325 1076,325 1095,378 671,378" fill="var(--gold)"/>
    <line x1="437" y1="0" x2="437" y2="446" stroke="#e3e3e3" stroke-width="1"/>
    <line x1="884" y1="0" x2="884" y2="446" stroke="#e3e3e3" stroke-width="1"/>
  </svg>

  <div class="brandline" style="left:536px;top:128px"><span class="mark"></span>Aramäische Gemeindekirche Wien-Nord – Hl. Ephräm in Wien</div>

  <div class="t verse-ref">Matthaeus<br>16:18</div>
  <p class="t verse">„Ich aber sage dir: Du bist Petrus, und auf diesen Felsen werde ich meine Kirche bauen, und die Mächte der Unterwelt werden sie nicht überwältigen.“</p>

  <p class="t pitch">Mit Ihrer Spende<br>leisten Sie einen wert-<br>vollen und nachhaltigen<br>Beitrag zur Errichtung und<br>Erhaltung der ältesten christli-<br>chen Urkirchen, in welcher noch<br>heute die Muttersprache Jesu gespro-<br>chen und weitergegeben wird.</p>
  <div class="t banner-title">IHRE SPENDE LOHNT SICH!</div>

  <div class="t account">
    <p>Unser Spendenkonto:</p>
    <p>Empfänger: Aramäische Gemeindekirche Wien-Nord<br>Bank: Donau Gemeindebank AG<br>IBAN: AT00 1234 5678 9012 3456<br>BIC: DOGBATWWXXX<br>Verwendung: SPENDE Kirchenbau von „Name des Spenders“</p>
    <p>Sehr gerne können Sie unser Projekt auch mit monatlichen<br>kleinen Beträgen mittels eines Dauerauftrags unterstützen.</p>
    <p>Eine Spendenbestätigung erhalten Sie jederzeit auf Anfrage<br>beim Pfarrgemeinderat der Kirche Hl. Ephräm.</p>
    <p class="thanks">Wir freuen und bedanken uns für jede Art von Zuwendung oder Unterstützung.</p>
  </div>

  <div class="t band-parish">Pfarrei Heiliger<br>Ephräm der Syrer</div>
  <div class="t band-appeal">Wir brauchen<br>IHRE Unterstützung!</div>
  <p class="t contact">Lindenhofer Platz 12<br>A-1210 Wien<br>kirche@st-ephraem-pfarre.at<br>www.st-ephraem-pfarre.at</p>
  <p class="t appeal-text">Beim ersten Neubau der<br>Aramäischen Gemeindekirche<br>in Österreich, in welcher die<br>Muttersprache Jesu gesprochen wird.</p>

  <div class="sheet sheet--inside"></div>
  <svg class="art art--inside" width="891" height="447" viewBox="0 0 891 447">
    <defs>
      <linearGradient id="panelSky" x1="0" y1="0" x2="0" y2="1">
        <stop offset="0" stop-color="var(--blue-panel)"/>
        <stop offset=".6" stop-color="var(--blue-panel-light)"/>
        <stop offset="1" stop-color="var(--blue-panel)"/>
      </linearGradient>
      <linearGradient id="nave" x1="0" y1="0" x2="0" y2="1">
        <stop offset="0" stop-color="#c9a243"/>
        <stop offset=".2" stop-color="#e3cf8e"/>
        <stop offset=".4" stop-color="#f4f2ee"/>
        <stop offset=".65" stop-color="#e9e3d8"/>
        <stop offset=".8" stop-color="#c79a62"/>
        <stop offset="1" stop-color="#eeeae2"/>
      </linearGradient>
      <linearGradient id="choir" x1="0" y1="0" x2="0" y2="1">
        <stop offset="0" stop-color="#7a2420"/>
        <stop offset=".35" stop-color="#c9b3ab"/>
        <stop offset=".6" stop-color="#f2efec"/>
        <stop offset="1" stop-color="#e6e0dc"/>
      </linearGradient>
    </defs>
    <rect x="0" y="0" width="891" height="447" fill="url(#panelSky)"/>
    <polygon points="200,0 732,0 451,270" fill="var(--white)" opacity=".35"/>
    <polygon role="img" aria-label="Innenansicht des Kirchenschiffs mit goldener Decke, Leuchtern und Holzbänken" points="232,0 670,0 451,207" fill="url(#nave)"/>
    <polygon points="0,228 30,228 300,447 264,447" fill="var(--white)" opacity=".35"/>
    <polygon points="891,224 860,224 612,447 645,447" fill="var(--white)" opacity=".35"/>
    <polygon role="img" aria-label="Foto des Kinder- und Jugendchors in weißen Gewändern am Notenpult" points="0,245 264,447 0,447" fill="url(#choir)"/>
    <polygon role="img" aria-label="Foto des Kinderchors in weißen Gewändern bei einem Auftritt" points="891,240 891,447 645,447" fill="url(#choir)"/>
  </svg>

  <h2 class="h who-h">WER SIND WIR?</h2>
  <div class="body who">
    <p>Wir sind eine christliche Minderheit aus dem Orient, welche in den letzten Jahrzehnten aufgrund von Kriegen und Christenverfolgungen in Österreich eine neue Heimat gefunden haben. Einige haben durch den Krieg ihre Familien, Häuser, Geschäfte, Grund und Boden verloren. Wir haben vieles verloren – nur unseren Glauben nicht.</p>
    <p>Die Aramäische Gemeindekirche ist eine der ältesten christlichen Urkirchen. In Österreich ist diese seit 1988 gesetzlich anerkannt. Die Liturgie wird bis heute in aramäischer Sprache, der Muttersprache Jesu gehalten.</p>
    <p>Für unsere Familien stellt die Integration keine allzu große Herausforderung dar. Wir lieben unsere neue Heimat und die deutsche Sprache zu erlernen hat für uns oberste Priorität. Wir schätzen die österreichische Kultur und Mentalität. Unser starker Integrationswille steht in keinem Gegensatz zur Bewahrung der eigenen Religion, Kultur und unserer aramäischen Sprache, der Muttersprache Jesu, welche zu den ältesten Sprachen der Welt gehört.</p>
  </div>

  <h2 class="h why-h">WARUM<br>BAUEN WIR<br>EINE KIRCHE?</h2>
  <div class="body why">
    <p>Die ersten verfolgten Christen unserer Gemeinde haben vor circa 50 Jahren in Österreich ein neues zu Hause gefunden. In dritter und vierter Generation leben derzeit ca. 1000 Familien in Österreich. Aufgrund der lebensgefährlichen Kriegszustände in Syrien und im Irak erfuhr unsere Kirche in Österreich vor allem in den letzten Jahren ein starkes Wachstum.</p>
    <p>Wir wollen mit unserem Kirchenbau zum einen dem Zuwachs christlicher Gläubigen gerecht werden, zum anderen das Christentum und seine christlichen Werte wieder stärken.</p>
    <p>Als christliche Urkirche haben wir eine große Verantwortung. Wir wollen für alle Gläubigen ein Zeichen der Hoffnung setzen und möchten den Menschen ein neues zu Hause geben, damit sie eine religiöse, kulturelle und gesellschaftliche Identifikation in ihrer neuen Heimat finden.</p>
    <p>Dieser besondere Kirchenbau ist ein historisches Ereignis.</p>
  </div>

  <h2 class="h proj-h">DAS<br>BAUPROJEKT<br>SELBST:</h2>
  <div class="body proj">
    <p>Das Kirchenbauprojekt befindet sich im 21. Wiener Gemeindebezirk, konkret an der Anschrift Lindenhofer Platz Nr. 12/14. In der ersten in Österreich gebauten Kirche unserer Gemeinschaft sollen über 350 Gläubige Platz finden.</p>
    <p>Auf diesem Areal befindet sich auch ein Kindergarten, der in Zusammenarbeit mit dem Diözesanverband Nord, der St. Clemens-Stiftung und unserer Pfarre Hl. Ephräm realisiert wurde. Der Kindergartenbetrieb wurde bereits aufgenommen und hat Platz für fast 80 Kinder unterschiedlicher Konfessionen geschaffen.</p>
    <p>Weiteres befindet sich auf unserem Areal ein Kulturzentrum mit Veranstaltungssaal, sowie Klassenzimmern für unsere traditionelle Samstagschule.</p>
    <p>Dieses Kirchen- und Kulturzentrum ist und wird insbesondere nach Fertigstellung zu einem wesentlichen Bestandteil und Lebensmittelpunkt für viele Familien, Kinder und Jugendliche werden.</p>
  </div>

  <h2 class="h do-h">WAS TUN WIR?</h2>
  <p class="body do-intro">Eine Vielzahl von gemeinnützigen, sozialen und kulturellen Aktivitäten, Schwerpunkten und Zielen…</p>
  <ul class="do-list">
    <li>wir helfen neu angekommenen Christen sich rasch zu integrieren</li>
    <li>wir unterstützen ehrenamtlich mit Dolmetsch-Tätigkeiten, Begleitung bei Behördenwegen, Suche von Schul- oder Kindergartenplätzen, Wohnungssuche und beim Erlernen der deutschen Sprache</li>
    <li>wir bieten Seelsorge insbesondere in schwierigen Lebensphasen oder bei Trauerbewältigung und kümmern uns um Menschen und Familien in Notlagen</li>
    <li>wir unterrichten Aramäisch, die Muttersprache Jesu und vermitteln soziale sowie christliche Werte</li>
    <li>wir fördern die Jugendarbeit und errichten mit dem Kirchenbau ein Jugendzentrum</li>
    <li>wir fördern Aktivitäten für unsere Kleinsten</li>
    <li>wir fördern Musiker durch eine eigene Musikband und einen Kinder-/ Jugendchor</li>
    <li>wir fördern die ökumenische Bewegung</li>
  </ul>

  <div class="brandline" style="left:340px;top:1043px"><span class="mark"></span>Aramäische Gemeindekirche Wien-Nord – Hl. Ephräm in Wien</div>

  <div class="form">
    <svg width="215" height="447" viewBox="0 0 215 447" font-family="Open Sans, Arial, sans-serif">
      <g fill="none" stroke="var(--form-red)" stroke-width=".8">
        <rect x="27" y="5" width="142" height="305" fill="var(--form-pink)" fill-opacity=".45"/>
        <line x1="45" y1="5" x2="45" y2="310"/>
        <line x1="63" y1="5" x2="63" y2="310"/>
        <line x1="80" y1="5" x2="80" y2="310"/>
        <line x1="97" y1="5" x2="97" y2="310"/>
        <line x1="115" y1="5" x2="115" y2="310"/>
        <line x1="132" y1="5" x2="132" y2="310"/>
        <line x1="150" y1="5" x2="150" y2="310"/>
        <rect x="63" y="5" width="17" height="124" stroke-width="1.2"/>
        <rect x="179" y="128" width="33" height="160"/>
      </g>
      <g fill="var(--form-red)" opacity=".35">
        <rect x="178" y="20" width="25" height="90"/>
      </g>
      <g fill="var(--form-red)" font-size="7">
        <text transform="translate(14,98) rotate(-90)" font-weight="700">ZAHLUNGSANWEISUNG</text>
        <text transform="translate(41,300) rotate(-90)" font-size="5">Empfänger</text>
        <text transform="translate(59,300) rotate(-90)" font-size="5">IBAN</text>
        <text transform="translate(76,300) rotate(-90)" font-size="5">BIC</text>
        <text transform="translate(76,125) rotate(-90)" font-weight="700" font-size="8">EUR</text>
        <text transform="translate(110,300) rotate(-90)" font-size="5">Verwendungszweck</text>
        <text transform="translate(145,300) rotate(-90)" font-size="5">Kontoinhaber</text>
        <text transform="translate(200,280) rotate(-90)" font-size="5">Unterschrift</text>
      </g>
      <text transform="translate(176,40) rotate(-90)" font-size="6" fill="var(--ink)" font-weight="700">006</text>
      <g fill="none" stroke="var(--ink)" stroke-width=".9">
        <rect x="26" y="323" width="186" height="118"/>
        <line x1="45" y1="323" x2="45" y2="441"/>
        <line x1="63" y1="323" x2="63" y2="441"/>
        <rect x="63" y="323" width="20" height="70" stroke-width="1.3"/>
        <line x1="100" y1="323" x2="100" y2="441"/>
        <line x1="118" y1="323" x2="118" y2="441"/>
        <line x1="135" y1="323" x2="135" y2="441"/>
      </g>
      <g fill="var(--ink)" font-size="5">
        <text transform="translate(16,438) rotate(-90)" font-size="6.5" font-weight="700">ZAHLUNGSANWEISUNG</text>
        <text transform="translate(23,430) rotate(-90)" font-size="6.5" font-weight="700">AUFTRAGSBESTÄTIGUNG</text>
        <text transform="translate(41,438) rotate(-90)">Empfänger</text>
        <text transform="translate(59,438) rotate(-90)">IBAN</text>
        <text transform="translate(79,390) rotate(-90)" font-weight="700" font-size="7">EUR</text>
        <text transform="translate(131,438) rotate(-90)">Verwendungszweck</text>
      </g>
      <text transform="translate(14,308) rotate(-90)" font-size="6" fill="var(--ink)" font-weight="700">AT</text>
    </svg>
  </div>

</div>
</body>
</html>
```